High end business card design for custom homebuilding company

Looking for a high end business card design that is unique and elegant. Can use embossing, foil printing, laser die cutting, or any high end printing technique or high end paper. Will upload current design so you can see the logo and what we are using currently, but we want something more unique and elegant. I included our logo to help with design.

Target Market(s)

High end custom home buyers of $1.5 million plus homes. Also real estate developers of high end communities.

Industry/Entity Type

Business

Contact Information for Business Card

Double sided. We want something very elegant and expensive looking. We are looking to incorporate a combination of perhaps linen paper or a high end paper, with foil stamping or embossing/debossing to make the card look unique, but still elegant. We tend to use blacks and golds, but are open to any ideas. Looking for creative and unique design.

Colors

Designer to choose colors to be used in the design.

Requirements
Must have
• High end, elegant look. Can use foil, embossing, or high end papers like linen. We want to make the card unique and interesting, but elegant and expensive looking.
Nice to have
• I am including just some cards I saw that looked interesting for one reason or another. I like a clean elegant design and like both the clean white style, and the blacks. So not sure if we want a black design or white. Would like to see both.

```html
<!DOCTYPE html>
<html lang="en">
<head>
<meta charset="utf-8">
<title>Larkspur Custom Homes – Business Card</title>
<link rel="stylesheet" href="https://fonts.googleapis.com/css2?family=Roboto:wght@400;500;700&display=swap">
<style>
  :root {
    --backdrop: #3b332e;
    --paper-white: #f1f1ef;
    --paper-black: #141416;
    --ink: #1c1b19;
    --ink-soft: #4a4946;
    --gold: #b9a23a;
    --gold-light: #d8c65a;
    --silver: #d4d4d4;
    --silver-dim: #8a8a8a;
  }
  * { box-sizing: border-box; margin: 0; padding: 0; }
  html, body {
    width: 1200px; height: 769px; overflow: hidden;
    background: var(--backdrop);
    font-family: "Roboto", Arial, sans-serif;
  }
  .canvas {
    position: relative; width: 1200px; height: 769px;
    display: flex; align-items: center; justify-content: center; gap: 60px;
  }
  .card {
    position: relative; width: 520px; height: 297px;
    border-radius: 3px;
    box-shadow: 0 10px 24px rgba(0,0,0,.45);
    overflow: hidden;
  }
  /* Front */
  .card--front { background: var(--paper-white); }
  .brand-mark-area {
    position: absolute; left: 26px; top: 30px; width: 238px; height: 238px;
    display: flex; align-items: center; justify-content: center;
  }
  .brand-ring {
    position: absolute; inset: 0; border-radius: 50%;
    border: 9px solid var(--ink);
  }
  .brand-mark-name {
    position: relative; text-align: center;
    font-weight: 700; font-size: 26px; line-height: 1.15; letter-spacing: 1px;
    color: var(--gold);
  }
  .contact {
    position: absolute; right: 30px; top: 34px; text-align: right;
    color: var(--ink-soft); font-size: 12.5px; line-height: 17px;
  }
  .contact__name { color: var(--gold); font-weight: 700; font-size: 17px; line-height: 20px; letter-spacing: .5px; }
  .contact__title { color: var(--ink); font-weight: 700; font-size: 12.5px; margin-bottom: 8px; }
  .contact__line { display: flex; justify-content: flex-end; align-items: center; gap: 6px; }
  .contact__line svg { width: 11px; height: 11px; flex: none; }
  .contact__spacer { width: 11px; flex: none; }
  .front-wordmark {
    position: absolute; right: 30px; bottom: 36px; text-align: right;
    font-weight: 500; color: var(--ink); font-size: 22px; letter-spacing: 1px; line-height: 1.1;
  }
  .front-wordmark span { display: block; font-size: 10px; letter-spacing: 4px; }
  /* Back */
  .card--back { background: var(--paper-black); display: flex; flex-direction: column; align-items: center; justify-content: center; }
  .back-wordmark {
    display: flex; align-items: center; gap: 12px;
    font-weight: 500; color: var(--silver); font-size: 34px; letter-spacing: 2px; line-height: 1;
  }
  .back-wordmark__dot { width: 34px; height: 34px; border-radius: 50%; border: 3px solid var(--silver); }
  .back-wordmark__sub { display: block; font-size: 11px; letter-spacing: 7px; margin-top: 6px; }
  .social-row { display: flex; gap: 8px; margin-top: 34px; }
  .social-row__dot { width: 16px; height: 16px; border-radius: 50%; background: var(--silver-dim); }
</style>
</head>
<body>
<main class="canvas">
  <section class="card card--front" aria-label="Card front">
    <div class="brand-mark-area">
      <div class="brand-ring"></div>
      <div class="brand-mark-name">LARKSPUR<br>CUSTOM<br>HOMES</div>
    </div>
    <div class="contact">
      <div class="contact__name">DANIEL HARTWELL</div>
      <div class="contact__title">CEO/FOUNDER</div>
      <div class="contact__line">2140 Birchwood Court<span class="contact__spacer"></span></div>
      <div class="contact__line">Fairbanks, Alaska 99701
        <svg viewBox="0 0 12 12" aria-hidden="true"><path fill="var(--gold)" d="M2.5 1h2l1 2.5-1.3 1a6 6 0 0 0 3.3 3.3l1-1.3L11 7.5v2a1 1 0 0 1-1 1A9 9 0 0 1 1.5 2a1 1 0 0 1 1-1z"/></svg></div>
      <div class="contact__line">907 555 0148
        <svg viewBox="0 0 12 12" aria-hidden="true"><rect x="1" y="2.5" width="10" height="7" rx="1" fill="var(--gold)"/><path d="M1.5 3l4.5 3.5L10.5 3" stroke="#fff" stroke-width="1" fill="none"/></svg></div>
      <div class="contact__line">daniel@larkspurhomes.com
        <svg viewBox="0 0 12 12" aria-hidden="true"><circle cx="6" cy="6" r="5" fill="var(--gold)"/><path d="M1 6h10M6 1c2 2.5 2 7.5 0 10M6 1c-2 2.5-2 7.5 0 10" stroke="#fff" stroke-width=".8" fill="none"/></svg></div>
      <div class="contact__line">www.larkspurhomes.com<span class="contact__spacer"></span></div>
    </div>
    <div class="front-wordmark">LARKSPUR<span>CUSTOM HOMES</span></div>
  </section>

  <section class="card card--back" aria-label="Card back">
    <div class="back-wordmark">
      <div class="back-wordmark__dot"></div>
      <div>LARKSPUR<span class="back-wordmark__sub">CUSTOM HOMES</span></div>
    </div>
    <div class="social-row" aria-label="Social profiles">
      <div class="social-row__dot"></div>
      <div class="social-row__dot"></div>
      <div class="social-row__dot"></div>
      <div class="social-row__dot"></div>
      <div class="social-row__dot"></div>
    </div>
  </section>
</main>
</body>
</html>
```